update of B2B website and conversion to single page

The current website needs to be modernized. I want what is commonly called a single page website. It is not actually a single page. See some examples here:
https://www.brivane.example/
https://www.quorel.example/
https://www.tindlewick.example/
Most or all graphics will be replaced.
Please see the attached spreadsheet for a rough draft of the home page layout. Convert the existing website at https://www.zolvinbyte.example/ to a single page website. We will provide the page content. You will provide all of the design, graphics, development, production deployment. etc. The look and feel should be corporate, polished, premium.

```html
<!DOCTYPE html>
<html lang="en">
<head>
<meta charset="utf-8">
<title>Zolvin Data — Enterprise Data Quality Made Easy</title>
<link href="https://fonts.googleapis.com/css2?family=Montserrat:wght@400;500;600;700;800;900&family=Lato:ital,wght@0,400;1,400&display=swap" rel="stylesheet">
<style>
:root{
  --sky:#6c9bcc;
  --navy:#2d3674;
  --yellow:#f2b51a;
  --ink:#333;
  --muted:#555;
  --card:#f8f8f8;
  --footer:#17213a;
  --footer-text:#b5bccb;
  --accent-blue:#3b7be0;
  --white:#fff;
}
*{margin:0;padding:0;box-sizing:border-box}
html,body{width:718px;height:1200px;overflow:hidden;background:var(--white)}
body{position:relative;font-family:"Montserrat",sans-serif;color:var(--ink)}
.abs{position:absolute}
.hero{left:0;top:0;width:718px;height:346px;background:var(--sky)}
.hero-art{left:16px;top:80px;width:316px;height:266px;background:linear-gradient(180deg,#b9d3ec 0%,#8fb3da 55%,#5c86b8 100%);border-radius:4px 4px 0 0}
.brand{left:80px;top:16px;display:flex;align-items:center;gap:6px;font-weight:700;font-size:17px;color:var(--yellow)}
.brand-mark{width:12px;height:12px;border-radius:50%;background:var(--navy)}
.brand-tag{left:98px;top:34px;font-size:6px;font-weight:700;color:var(--navy)}
.contact{display:flex;gap:8px;align-items:center;color:var(--white);font-size:6.5px;font-weight:600;line-height:1.35}
.contact span{display:block;color:var(--yellow);font-weight:500}
.contact .sep{width:1px;height:18px;background:rgba(0,0,0,.35)}
.nav{left:81px;top:54px;width:561px;height:24px;background:var(--navy);display:flex;align-items:center}
.nav a{color:var(--white);font-size:7.5px;font-weight:600;text-decoration:none;margin-right:15px}
.nav a:first-child{margin-left:23px;position:relative}
.nav a:first-child::after{content:"";position:absolute;left:0;right:0;bottom:-8px;height:2px;background:var(--yellow)}
.trial{left:562px;top:54px;width:80px;height:24px;background:var(--yellow);color:var(--navy);font-size:7.5px;font-weight:700;display:flex;align-items:center;justify-content:center}
.hero-title{left:300px;top:168px;width:380px;text-align:center;color:var(--white);font-weight:700;font-size:24px;letter-spacing:-.5px}
.hero-sub{left:300px;top:200px;width:380px;text-align:center;color:var(--white);font-size:11px}
.btn{background:var(--yellow);color:var(--ink);font-weight:700;font-size:5.5px;border-radius:12px;display:flex;align-items:center;justify-content:center;text-transform:uppercase}
.cards{left:79px;top:323px;width:561px;height:111px;background:var(--card);box-shadow:0 2px 8px rgba(0,0,0,.12);display:flex}
.card{padding:28px 0 0 46px;border-right:1px solid #e4e4e4}
.card:last-child{border-right:0}
.card h3{display:flex;align-items:center;gap:6px;font-size:10px;font-weight:600;color:var(--yellow);margin-left:-1px}
.card p{font-family:"Lato",sans-serif;font-style:italic;font-size:6.5px;color:var(--muted);line-height:1.75;margin-top:7px;width:148px}
.card .more{font-size:6px;font-weight:600;margin-top:7px;color:var(--ink)}
h2{font-weight:900;font-size:17.5px;color:#2b2b2b;letter-spacing:-.2px}
.copy{font-family:"Lato",sans-serif;font-style:italic;font-size:6.6px;color:var(--muted);line-height:1.72;width:290px}
.copy p+p{margin-top:11px}
.art-a{left:440px;top:466px;width:200px;height:150px;border-radius:48% 52% 46% 54%;background:radial-gradient(circle at 50% 50%,#d9ecf8 0%,#eef5fb 70%)}
.art-b{left:72px;top:640px;width:204px;height:152px;border-radius:52% 48% 50% 50%;background:radial-gradient(circle at 45% 50%,#9fd8f2 0%,#eef5fb 70%)}
.video-title{left:0;top:822px;width:718px;text-align:center}
.video{left:0;top:850px;width:718px;height:145px;background:linear-gradient(100deg,#0f1720 0%,#16323a 50%,#1f6b6a 80%,#0f1720 100%)}
.play{left:367px;top:915px;width:30px;height:30px;border-radius:50%;background:var(--white);display:flex;align-items:center;justify-content:center}
.footer{left:0;top:995px;width:718px;height:205px;background:var(--footer)}
.fcol{top:1040px;color:var(--footer-text);font-size:7px;line-height:11.6px}
.fcol h4{color:var(--white);font-size:7.3px;font-weight:500;letter-spacing:.3px;margin-bottom:7px}
.fcol .lead{color:var(--white)}
.social{display:grid;grid-template-columns:60px 60px}
.rule{left:37px;top:1147px;width:654px;height:1px;background:#3a4560}
.up{left:352px;top:1135px;width:24px;height:24px;border-radius:50%;background:var(--accent-blue);display:flex;align-items:center;justify-content:center}
.copyright{left:0;top:1175px;width:718px;text-align:center;font-size:6.5px;color:var(--footer-text)}
</style>
</head>
<body>
<header>
  <div class="abs hero"></div>
  <div class="abs hero-art" role="img" aria-label="Illustration of cloud servers with connected clouds and gears"></div>
  <div class="abs brand"><i class="brand-mark"></i>Zolvin Data</div>
  <div class="abs brand-tag">Enterprise Data Quality Made Easy</div>
  <div class="abs contact" style="left:451px;top:20px">
    <i class="sep"></i>
    <svg width="14" height="10" viewBox="0 0 14 10"><rect x=".5" y=".5" width="13" height="9" fill="none" stroke="#fff"/><path d="M.5 .5 7 6l6.5-5.5" fill="none" stroke="#fff"/></svg>
    <div>Contact Email<span>info@zolvinbyte.example</span></div>
    <i class="sep" style="margin-left:16px"></i>
    <svg width="11" height="12" viewBox="0 0 11 12"><path d="M2 1l2 2.5-1.2 1.4a6 6 0 0 0 3.3 3.3L7.5 7 10 9l-1.3 2C4.5 10.5 1 7 .8 2.5z" fill="none" stroke="#fff"/></svg>
    <div>Phone Number<span style="font-weight:700">(555) 013-4593</span></div>
  </div>
  <nav class="abs nav">
    <a href="#">Services</a><a href="#">Connectors</a><a href="#">Features</a><a href="#">Why QS*Plus?</a><a href="#">Offers</a><a href="#">Blog</a><a href="#">Company</a>
    <svg style="margin-left:75px" width="7" height="7" viewBox="0 0 7 7"><circle cx="3" cy="3" r="2.2" fill="none" stroke="#fff" stroke-width="1.1"/><path d="M4.6 4.6 6.5 6.5" stroke="#fff" stroke-width="1.1"/></svg>
  </nav>
  <div class="abs trial">Free Trail</div>
  <h1 class="abs hero-title">Data Quality Proof of Concept</h1>
  <div class="abs hero-sub">Data Concept // Data Cleansing // Novabase</div>
  <div class="abs btn" style="left:460px;top:228px;width:64px;height:20px">Sign up now!</div>
</header>

<section class="abs cards">
  <div class="card" style="width:197px">
    <h3><svg width="18" height="16" viewBox="0 0 18 16"><path d="M4 11a3.5 3.5 0 0 1 .5-7 5 5 0 0 1 9.5 1.5A3 3 0 0 1 13.5 11" fill="none" stroke="#555"/><rect x="6" y="9" width="6" height="5" fill="none" stroke="#555"/></svg>Zolvin Data</h3>
    <p>The QS*Plus RelayBase Database Connector eliminates the need for custom integration</p>
    <div class="more">Read More &nbsp;&nbsp;&nbsp; ....</div>
  </div>
  <div class="card" style="width:177px;padding-left:27px">
    <h3><svg width="18" height="18" viewBox="0 0 18 18"><rect x="2" y="3" width="11" height="14" fill="none" stroke="#555"/><path d="M5 9l3 3 8-10" fill="none" stroke="#555" stroke-width="1.3"/></svg>Data Quality</h3>
    <p>QS*Plus Batch works in the background, cleansing data, and identifying and merging</p>
    <div class="more">Read More &nbsp;&nbsp;&nbsp; ....</div>
  </div>
  <div class="card" style="width:187px;padding-left:30px">
    <h3><svg width="18" height="18" viewBox="0 0 18 18"><ellipse cx="9" cy="4" rx="7" ry="2.3" fill="none" stroke="#555"/><path d="M2 4v10c0 1.3 3 2.3 7 2.3s7-1 7-2.3V4M2 7.5c0 1.3 3 2.3 7 2.3s7-1 7-2.3M2 11c0 1.3 3 2.3 7 2.3s7-1 7-2.3" fill="none" stroke="#555"/></svg>Corvane Connector</h3>
    <p>The QS*Plus Corvane Connector eliminates integration work, saving your business time</p>
    <div class="more">Read More &nbsp;&nbsp;&nbsp; ....</div>
  </div>
</section>

<section>
  <h2 class="abs" style="left:80px;top:479px">Who We Are What We Do</h2>
  <div class="abs copy" style="left:80px;top:510px">
    <p>Zolvin Data was founded in 1998 as a consulting company focused on the implementation of enterprise applications. Our team was comprised of senior software developers who had worked for many of the leading commercial application vendors.</p>
    <p>Our customer's relied heavily on their applications and quickly became aware that their level of success was dependent on the quality of their data. Increasingly these customers asked Zolvin Data to solve their data quality problems.</p>
  </div>
  <div class="abs btn" style="left:78px;top:605px;width:65px;height:20px">Read more</div>
  <div class="abs art-a" role="img" aria-label="Illustration of server racks, cloud and monitor with gear icons"></div>
</section>

<section>
  <div class="abs art-b" role="img" aria-label="Illustration of data cleaning cloud with server units"></div>
  <h2 class="abs" style="left:347px;top:657px">Why Choose Us?</h2>
  <div class="abs copy" style="left:347px;top:688px">
    <p>Zolvin Data was founded in 1998 as a consulting company focused on the implementation of enterprise applications. Our team was comprised of senior software developers who had worked for many of the leading commercial application vendors.</p>
    <p>Our customer's relied heavily on their applications and quickly became aware that their level of success was dependent on the quality of their data. Increasingly these customers asked Zolvin Data to solve their data quality problems.</p>
  </div>
</section>

<section>
  <h2 class="abs video-title">See Video of &nbsp;Data Quality</h2>
  <div class="abs video" role="img" aria-label="Video still of streaming binary data"></div>
  <div class="abs play"><svg width="12" height="13" viewBox="0 0 12 13"><path d="M1 .5 11.5 6.5 1 12.5z" fill="#222"/></svg></div>
</section>

<footer>
  <div class="abs footer"></div>
  <div class="abs fcol" style="left:80px;width:130px">
    <h4>OUR SERVICES</h4>
    Zolvin Data consultants are Customer Data experts. We provide high value services to solve your biggest data challenges.
    <div class="lead" style="margin-top:3px">Reda more...</div>
  </div>
  <div class="abs fcol" style="left:238px">
    <h4>COMPANY</h4>
    Services<br>Connectors<br>Features<br>FAQs<br>Offers<br>Company
  </div>
  <div class="abs fcol" style="left:358px">
    <h4>CONTCT US</h4>
    Location: Zolvin Data<br>418 Larkfield Way<br>Suite 200, Cedar Vale, CA 90021
    <div style="margin-top:6px">Tel: (555) 013-4593<br>Email: info@zolvinbyte.example</div>
  </div>
  <div class="abs fcol" style="left:515px">
    <h4>FOLLOW US</h4>
    <div class="social"><span>Friendwall</span><span>Shotboard</span><span>Chirpline</span><span>Portfolix</span><span>Snapgrid</span><span>Pinstack</span><span>Linkwork</span></div>
  </div>
  <div class="abs rule"></div>
  <div class="abs up"><svg width="8" height="5" viewBox="0 0 8 5"><path d="M1 4 4 1l3 3" fill="none" stroke="#fff"/></svg></div>
  <div class="abs copyright">Copyright © 2018 Zolvin Data</div>
</footer>
</body>
</html>
```